【 概要 】 都内で7年目のイタリアンレストランです。 コロナ渦でテイクアウト営業に勤しんでおります。 今までスタッフが書いたチラシで頑張ってましたが、メニュー改訂もあり是非プロのお力添えを頂きたく募集致しました。 素敵なデザインを楽しみにしております。 【 依頼内容 】 ・サイズ:A4 片面 ・ページ数:1ページ ・素材の用意(画像・文章等):添付ファイル1枚目がメニューです ・デザイン内容:添付ファイル2枚目がイメージです。料理や人物を参考にお願いします 【 デザインイメージ 】 ・ターゲット層:都心在住の30〜50代男女 ・雰囲気:ナチュラルでおしゃれな雰囲気 ・参考デザイン: お店のイメージ(URL参考)添付ファイル2枚目参照 【 契約金額(税抜) 】 2万円 ※契約金額(税込)からシステム利用料を差し引いた金額が、ワーカーさまの受取金額となります その他ご質問等ありましたら、気軽にお問い合わせください。 ご応募をお待ちしております! |
| https://find.kumoriba.co.jp/amp/s/s.shokunavi-ranpo.jp/tokyo/B2401/B240305/24085917/top_amp/%3Fusqp%3Dxr482KZTMBHZBafV9N3q9-vY6RHxBTB%253D | ||
この度は有難うございます。また細かな修正も早急に対応してくださりありがたかったです。お陰で妥協なくイメージしたデザインに仕上がりました。スキルも高く誠意も伝わりとても感謝致します。また機会がございましたら宜しくお願い致します。
この度は皆様素敵なデザインをありがとうございました!皆様の素敵なデザインに感動し感謝の気持ちでいっぱいでした。コロナ渦で皆様も大変な状況だと思いますが、私も頑張ろうという気持ちになりました。心からありがとうございました。

```html
<!DOCTYPE html>
<html lang="ja">
<head>
<meta charset="utf-8">
<title>TRATTORIA VENTO テイクアウトメニュー</title>
<link rel="stylesheet" href="https://fonts.googleapis.com/css2?family=Zen+Maru+Gothic:wght@500;700&family=Yusei+Magic&family=Alfa+Slab+One&family=Playfair+Display:wght@700&display=swap">
<style>
:root{
  --stage:#c9c9c9;
  --ink:#151515;
  --panel:#e7e6e2;
  --paper:#ffffff;
  --text:#1d1d1d;
}
*{margin:0;padding:0;box-sizing:border-box}
html,body{width:984px;height:1200px;overflow:hidden;background:var(--stage)}
.flyer{position:absolute;left:93px;top:35px;width:800px;height:1130px;overflow:hidden;
  font-family:"Zen Maru Gothic",sans-serif;color:var(--text)}
.backdrop{position:absolute;inset:0;background:
  radial-gradient(circle at 8% 12%,rgba(200,50,31,.55) 0 40px,transparent 80px),
  radial-gradient(circle at 94% 6%,rgba(200,50,31,.5) 0 36px,transparent 70px),
  radial-gradient(circle at 4% 62%,rgba(79,138,44,.55) 0 60px,transparent 130px),
  radial-gradient(circle at 97% 58%,rgba(79,138,44,.5) 0 50px,transparent 110px),
  radial-gradient(circle at 90% 96%,rgba(200,50,31,.45) 0 40px,transparent 90px),
  radial-gradient(circle at 10% 96%,rgba(210,180,110,.35) 0 50px,transparent 110px),
  var(--ink)}
.panel{position:absolute;left:0;top:0}
.brand{position:absolute;left:0;width:800px;text-align:center;color:var(--ink)}
.brand-sub{top:28px;font:700 15px "Playfair Display",serif;letter-spacing:2px}
.brand-name{top:46px;font:700 44px "Playfair Display",serif;letter-spacing:3px}
.headline{position:absolute;left:200px;top:175px;width:400px;height:150px}
.headline-text{position:absolute;left:0;width:400px;text-align:center;color:var(--paper);font-family:"Yusei Magic",sans-serif;white-space:nowrap}
.takeout{top:4px;font-size:74px;line-height:90px;letter-spacing:3px}
.can-do{top:94px;font-size:36px;line-height:46px;letter-spacing:4px}
.col{position:absolute;top:0;height:1130px}
.col-left{left:58px;width:344px}
.col-right{left:428px;width:314px}
.ribbon{position:absolute;left:50%;margin-left:-125px;width:250px;height:36px;background:var(--ink);color:var(--paper);
  clip-path:polygon(0 0,100% 0,94% 50%,100% 100%,0 100%,6% 50%);
  font:16px "Alfa Slab One",serif;letter-spacing:2px;display:flex;align-items:center;justify-content:center}
.note{position:absolute;left:0;width:100%;text-align:center;font-size:12px;line-height:16px;font-weight:500}
.menu{position:absolute;left:0;width:100%;list-style:none}
.menu li{display:flex;justify-content:space-between;height:28px;align-items:center;font-size:14px;font-weight:700;
  white-space:nowrap;border-bottom:1px dotted rgba(0,0,0,.25)}
.menu li span:first-child{overflow:hidden}
.menu li span:last-child{flex:none;padding-left:8px}
.reserve{position:absolute;left:428px;top:862px;width:314px;height:184px;border:2px solid var(--ink);border-radius:6px;
  text-align:center;background:rgba(255,255,255,.55)}
.reserve-head{margin-top:12px;font:22px/1.25 "Yusei Magic",sans-serif}
.reserve-name{margin-top:6px;font-size:12px;font-weight:700}
.reserve-tel{margin-top:4px;display:flex;align-items:center;justify-content:center;gap:8px;font:700 30px "Zen Maru Gothic",sans-serif;letter-spacing:1px}
.reserve-hours{margin-top:4px;font-size:13px;font-weight:700}
.reserve-foot{font-size:10.5px}
</style>
</head>
<body>
<div class="flyer">
  <div class="backdrop" role="img" aria-label="黒板風の背景にトマト、バジル、パスタなどの食材イラスト"></div>

  <svg class="panel" width="800" height="1130" viewBox="0 0 800 1130" aria-hidden="true">
    <path d="M60 150 H187 V37 Q187 10 214 10 H586 Q613 10 613 37 V150 H740 Q767 150 767 177 V1055 Q767 1082 740 1082 H60 Q33 1082 33 1055 V177 Q33 150 60 150 Z"
      fill="var(--panel)" stroke="#f4f4f1" stroke-width="3"/>
    <path d="M218 175 H582 L598 252 L582 328 H218 L202 252 Z" fill="var(--ink)"/>
  </svg>

  <div class="brand brand-sub">TRATTORIA</div>
  <div class="brand brand-name">VENTO</div>

  <div class="headline">
    <div class="headline-text takeout">TAKE OUT</div>
    <div class="headline-text can-do">できます!</div>
  </div>

  <section class="col col-left">
    <div class="ribbon" style="top:370px">ANTIPASTO</div>
    <ul class="menu" style="top:416px">
      <li><span>アンチョビポテト</span><span>¥500</span></li>
      <li><span>ゴルゴンゾーラのキッシュ(2ピース)</span><span>¥500</span></li>
      <li><span>ピクルス&amp;オリーブ</span><span>¥500</span></li>
      <li><span>合鴨のロースト</span><span>¥800</span></li>
      <li><span>いわしのトマト煮</span><span>¥950</span></li>
      <li><span>ローストビーフ</span><span>¥1,200</span></li>
      <li><span>ローストポーク</span><span>¥1,200</span></li>
    </ul>

    <div class="ribbon" style="top:640px">PASTA</div>
    <div class="note" style="top:682px">麺は全てリングイネです</div>
    <ul class="menu" style="top:702px">
      <li><span>はまぐりと大根おろしのボンゴレビアンコ</span><span>¥1,200</span></li>
      <li><span>わたりがにのトマトクリーム</span><span>¥1,500</span></li>
      <li><span>にんにくとアンチョビのペペロンチーノ</span><span>¥1,000</span></li>
      <li><span>ゴルゴンゾーラのペンネ</span><span>¥1,000</span></li>
      <li><span>アラビアータのペンネ</span><span>¥1,000</span></li>
    </ul>

    <div class="ribbon" style="top:862px">SPECIALITA</div>
    <ul class="menu" style="top:908px">
      <li><span>天使の海老クリーム煮</span><span>¥1,500</span></li>
      <li><span>つぶ貝と小海老エスカルゴバター</span><span>¥1,200</span></li>
      <li><span>魚介と旨み細麺アヒージョ(スープ仕立て)</span><span>¥1,000</span></li>
      <li><span>サザエ</span><span>¥1,000</span></li>
      <li><span>バケット 2ピース</span><span>¥300</span></li>
    </ul>
  </section>

  <section class="col col-right">
    <div class="ribbon" style="top:370px">PIZZA</div>
    <ul class="menu" style="top:416px">
      <li><span>マルゲリータ</span><span>¥1,500</span></li>
      <li><span>クアトロフォルマッジョ</span><span>¥1,500</span></li>
      <li><span>博多明太子のピッツァ</span><span>¥1,800</span></li>
      <li><span>ザ・サルシッチャ</span><span>¥1,800</span></li>
    </ul>

    <div class="ribbon" style="top:546px">INSALATA</div>
    <div class="note" style="top:588px">3〜4名分</div>
    <ul class="menu" style="top:606px">
      <li><span>生ハムのグリーンサラダ</span><span>¥1,500</span></li>
      <li><span>イタリアン白インゲンサラダ</span><span>¥1,000</span></li>
      <li><span>VENTO のシーザーサラダ</span><span>¥1,000</span></li>
      <li><span>フレンチサラダ(Sサイズ)</span><span>¥450</span></li>
    </ul>

    <div class="ribbon" style="top:738px">DOLCE</div>
    <ul class="menu" style="top:784px">
      <li><span>ガトーショコラ</span><span>¥500</span></li>
      <li><span>ティラミス</span><span>¥500</span></li>
    </ul>
  </section>

  <div class="reserve">
    <div class="reserve-head">前日ご予約<br>お願いいたします。</div>
    <div class="reserve-name">TRATTORIA VENTO(トラットリア ヴェント)</div>
    <div class="reserve-tel">
      <svg width="28" height="28" viewBox="0 0 24 24" aria-hidden="true"><path fill="#151515" d="M6.6 10.8a15.1 15.1 0 0 0 6.6 6.6l2.2-2.2a1 1 0 0 1 1-.25 11.4 11.4 0 0 0 3.6.57 1 1 0 0 1 1 1V20a1 1 0 0 1-1 1A17 17 0 0 1 3 4a1 1 0 0 1 1-1h3.5a1 1 0 0 1 1 1c0 1.25.2 2.45.57 3.57a1 1 0 0 1-.25 1z"/></svg>
      03-5550-1234
    </div>
    <div class="reserve-hours">テイクアウト 16:00〜21:00</div>
    <div class="reserve-foot">(土日祝はランチも承ります)</div>
  </div>
</div>
</body>
</html>
```